Need a book cover design for a Lumora Book

Book has a long title and sub title so lots of words to fit on the cover.

I can be flexible a bit with the sub title due to the length of it but ideally i can get a design that takes everything.

Here is the title:

Tidal Geology: The Roots of Erosion, Sedimentation, and Canyon Forming

Sub Title/Heading
An Easy Primer on Coastal Cliffs, Dune Drift, River Beds, and Delta Mapping Methods

```html
<!DOCTYPE html>
<html lang="en">
<head>
<meta charset="utf-8">
<title>Tidal Geology — Book Cover</title>
<link rel="stylesheet" href="https://fonts.googleapis.com/css2?family=Didact+Gothic&family=Questrial&display=swap">
<style>
  :root {
    --stage-pink: #f5566f;
    --cover-yellow: #f0c20a;
    --cover-amber: #e79a2c;
    --cover-orange: #e0704a;
    --cover-crimson: #da1a4e;
    --pill-crimson: #d81a4d;
    --pill-orange: #df7a42;
    --pill-yellow: #ebc10b;
    --spine-line: rgba(120, 80, 20, 0.55);
    --ink-white: #f6f4f2;
  }

  * { box-sizing: border-box; margin: 0; padding: 0; }

  html, body {
    width: 1200px;
    height: 900px;
    overflow: hidden;
    background: var(--stage-pink);
  }

  .stage {
    position: relative;
    width: 1200px;
    height: 900px;
  }

  .book-cover {
    position: absolute;
    left: 300px;
    top: 60px;
    width: 600px;
    height: 780px;
    overflow: hidden;
    background: linear-gradient(
      to bottom,
      var(--cover-yellow) 0%,
      var(--cover-yellow) 38%,
      var(--cover-amber) 60%,
      var(--cover-orange) 80%,
      var(--cover-crimson) 100%
    );
  }

  .spine-fold {
    position: absolute;
    left: 26px;
    top: 0;
    width: 2px;
    height: 100%;
    background: var(--spine-line);
  }

  .spine-fold::before {
    content: "";
    position: absolute;
    left: -26px;
    top: 0;
    width: 26px;
    height: 100%;
    background: linear-gradient(to right, rgba(255, 220, 60, 0.25), rgba(0, 0, 0, 0.04));
  }

  .capsule {
    position: absolute;
    left: 196px;
    top: 112px;
    width: 210px;
    height: 540px;
    border-radius: 105px;
    background: linear-gradient(
      to bottom,
      var(--pill-crimson) 0%,
      #d9484a 20%,
      var(--pill-orange) 45%,
      #e39a35 62%,
      var(--pill-yellow) 78%,
      var(--pill-yellow) 100%
    );
  }

  .title-block {
    position: absolute;
    left: 0;
    top: 318px;
    width: 100%;
    text-align: center;
    color: var(--ink-white);
  }

  .book-title {
    font-family: "Questrial", sans-serif;
    font-weight: 400;
    font-size: 58px;
    letter-spacing: 1px;
    line-height: 1;
    padding-left: 70px;
  }

  .book-subtitle {
    margin-top: 10px;
    font-family: "Didact Gothic", sans-serif;
    font-size: 22px;
    line-height: 1.2;
    padding-left: 30px;
  }

  .author-name {
    position: absolute;
    right: 52px;
    top: 598px;
    font-family: "Questrial", sans-serif;
    font-size: 13px;
    color: var(--ink-white);
  }

  .tagline {
    position: absolute;
    left: 58px;
    top: 662px;
    width: 200px;
    font-family: "Didact Gothic", sans-serif;
    font-size: 14px;
    line-height: 1.2;
    color: var(--ink-white);
  }
</style>
</head>
<body>
  <main class="stage">
    <article class="book-cover">
      <div class="spine-fold"></div>
      <div class="capsule"></div>

      <header class="title-block">
        <h1 class="book-title">TIDAL GEOLOGY</h1>
        <p class="book-subtitle">The Roots of Erosion,<br>Sedimentation, and<br>Canyon Forming</p>
      </header>

      <p class="author-name">Authors Name(s)</p>

      <p class="tagline">An Easy Primer on Coastal Cliffs, Dune Drift, River Beds, and Delta Mapping Methods</p>
    </article>
  </main>
</body>
</html>
```